An our door sign really promoting our clinic and services

We have a new sports medicine clinic called HALLCREST SPORTS MEDICINE.
We want to make a really nice external sign at our clinic using a photo of our team we really like. I have attached the photo.
We want to simply include our LOGO and also signs with these slogan options. So we want different signs with these different slogans so we can choose what we really like.
This should be a simple and quite design.

The SLOGANS WE WOULD LIKE TO SEE ON THE SIGN (only one slogan per sign in the drafts)

1. Your Journey. Our Expertise
2. Where better health begins
3. Building the best version of you
4. Your health, in expert hands
5. Reaching new heights in your health
6. Your path to peak performance starts here

I have also included different versions of our logo based on the background and how you set the sign up

So summary
1. Image attached
2. Slogan options we would like to see them all
3. Logo attached (various options based on how you set the background up)
4. Size of sign is 2935mm wide x 1885mm high

```html
<!DOCTYPE html>
<html lang="en">
<head>
<meta charset="utf-8">
<title>Hallcrest Sports Medicine – Exterior Sign Options</title>
<link href="https://fonts.googleapis.com/css2?family=Oswald:wght@500;600&display=swap" rel="stylesheet">
<style>
  :root {
    --navy: #151a4e;
    --white: #ffffff;
    --accent: #2bb8ea;
    --board-light: #ffffff;
    --board-dark: #c9c9cc;
    --photo-dark: #2a2f3c;
    --photo-mid: #6b6e72;
    --photo-light: #b9a98a;
    --turf: #4e7a3a;
  }
  * { margin: 0; padding: 0; box-sizing: border-box; }
  html, body { width: 1200px; height: 600px; overflow: hidden; }
  body {
    position: relative;
    background: linear-gradient(100deg, var(--board-light) 0%, #eeeeef 40%, var(--board-dark) 100%);
    font-family: "Oswald", "Arial Narrow", sans-serif;
  }
  .sign {
    position: absolute;
    width: 374px;
    height: 240px;
    background: var(--navy);
    overflow: hidden;
    box-shadow: 3px 5px 8px rgba(0,0,0,0.28);
  }
  .row-1 { top: 52px; }
  .row-2 { top: 305px; }
  .col-1 { left: 24px; }
  .col-2 { left: 413px; }
  .col-3 { left: 797px; }
  .sign__photo {
    position: absolute;
    inset: 0;
    width: 374px;
    height: 240px;
  }
  .brand {
    position: absolute;
    left: 14px;
    top: 38px;
    display: flex;
    align-items: center;
    gap: 8px;
    color: var(--white);
    font-weight: 600;
  }
  .brand__dot {
    width: 14px;
    height: 14px;
    border-radius: 50%;
    background: var(--accent);
  }
  .brand__name {
    display: flex;
    flex-direction: column;
    line-height: 1;
  }
  .brand__main { font-size: 17px; letter-spacing: 1px; }
  .brand__sub { font-size: 7px; letter-spacing: 3px; margin-top: 2px; }
  .slogan {
    position: absolute;
    left: 29px;
    color: var(--white);
    font-weight: 600;
    line-height: 1.02;
    font-size: 24px;
  }
  .slogan span { display: block; }
  .slogan--journey { top: 98px; }
  .slogan--better { top: 100px; }
  .slogan--version { top: 98px; }
  .slogan--hands { top: 108px; }
  .slogan--hands .lead { font-size: 29px; line-height: 1.05; }
  .slogan--hands .tail { font-size: 20px; }
  .slogan--heights { top: 96px; font-size: 25px; line-height: 0.98; }
  .slogan--heights .tail { font-size: 23px; }
  .slogan--peak { top: 104px; font-size: 25px; line-height: 1.0; }
  .slogan--peak .lead { font-size: 18px; line-height: 1.2; }
</style>
</head>
<body>

<svg width="0" height="0" style="position:absolute">
  <defs>
    <linearGradient id="photoTone" x1="0" y1="0" x2="0" y2="1">
      <stop offset="0" stop-color="#8c8577"/>
      <stop offset="0.45" stop-color="#3a3e4a"/>
      <stop offset="0.85" stop-color="#2a2f3c"/>
      <stop offset="1" stop-color="#4e7a3a"/>
    </linearGradient>
  </defs>
</svg>

<!-- Sign 1 -->
<section class="sign row-1 col-1">
  <svg class="sign__photo" viewBox="0 0 374 240" role="img" aria-label="Photo of two clinicians in the gym, one holding a tablet while the other listens">
    <path d="M236 0 C196 60 168 150 172 240 L374 240 L374 0 Z" fill="url(#photoTone)"/>
  </svg>
  <div class="brand"><div class="brand__dot"></div><div class="brand__name"><span class="brand__main">HALLCREST</span><span class="brand__sub">SPORTS MEDICINE</span></div></div>
  <h2 class="slogan slogan--journey"><span>Your Journey</span><span>Our Expertise</span></h2>
</section>

<!-- Sign 2 -->
<section class="sign row-1 col-2">
  <svg class="sign__photo" viewBox="0 0 374 240" role="img" aria-label="Photo of two clinicians in the gym, one holding a tablet while the other listens">
    <path d="M236 0 C196 60 168 150 172 240 L374 240 L374 0 Z" fill="url(#photoTone)"/>
  </svg>
  <div class="brand"><div class="brand__dot"></div><div class="brand__name"><span class="brand__main">HALLCREST</span><span class="brand__sub">SPORTS MEDICINE</span></div></div>
  <h2 class="slogan slogan--better"><span>Where Better</span><span>Health Begins</span></h2>
</section>

<!-- Sign 3 -->
<section class="sign row-1 col-3">
  <svg class="sign__photo" viewBox="0 0 374 240" role="img" aria-label="Photo of two clinicians in the gym, one holding a tablet while the other listens">
    <path d="M236 0 C196 60 168 150 172 240 L374 240 L374 0 Z" fill="url(#photoTone)"/>
  </svg>
  <div class="brand"><div class="brand__dot"></div><div class="brand__name"><span class="brand__main">HALLCREST</span><span class="brand__sub">SPORTS MEDICINE</span></div></div>
  <h2 class="slogan slogan--version"><span>Building the</span><span>Best Version</span><span>of You</span></h2>
</section>

<!-- Sign 4 -->
<section class="sign row-2 col-1">
  <svg class="sign__photo" viewBox="0 0 374 240" role="img" aria-label="Photo of two clinicians in the gym, one holding a tablet while the other listens">
    <path d="M236 0 C196 60 168 150 172 240 L374 240 L374 0 Z" fill="url(#photoTone)"/>
  </svg>
  <div class="brand"><div class="brand__dot"></div><div class="brand__name"><span class="brand__main">HALLCREST</span><span class="brand__sub">SPORTS MEDICINE</span></div></div>
  <h2 class="slogan slogan--hands"><span class="lead">Your health</span><span class="tail">in expert hands</span></h2>
</section>

<!-- Sign 5 -->
<section class="sign row-2 col-2">
  <svg class="sign__photo" viewBox="0 0 374 240" role="img" aria-label="Photo of two clinicians in the gym, one holding a tablet while the other listens">
    <path d="M236 0 C196 60 168 150 172 240 L374 240 L374 0 Z" fill="url(#photoTone)"/>
  </svg>
  <div class="brand"><div class="brand__dot"></div><div class="brand__name"><span class="brand__main">HALLCREST</span><span class="brand__sub">SPORTS MEDICINE</span></div></div>
  <h2 class="slogan slogan--heights"><span>Reaching</span><span>New Heights</span><span class="tail">in Your Health</span></h2>
</section>

<!-- Sign 6 -->
<section class="sign row-2 col-3">
  <svg class="sign__photo" viewBox="0 0 374 240" role="img" aria-label="Photo of two clinicians in the gym, one holding a tablet while the other listens">
    <path d="M236 0 C196 60 168 150 172 240 L374 240 L374 0 Z" fill="url(#photoTone)"/>
  </svg>
  <div class="brand"><div class="brand__dot"></div><div class="brand__name"><span class="brand__main">HALLCREST</span><span class="brand__sub">SPORTS MEDICINE</span></div></div>
  <h2 class="slogan slogan--peak"><span class="lead">Your Path to Peak</span><span>Performance</span><span>Starts Here</span></h2>
</section>

</body>
</html>
```